Email Signature Gif Animation Design

We are looking for an interactive Email Signature to Standardize around for our growing company.

We are a commerical electrical contractor based out of North Jersey. We have a big corporate client tele and perfer a more professional fresh looking signature with titles and perhaps a suttle animation for effect.

Attached below is our company logo which is to be used prominently in the emai signature. We would consider a "refresh' of our logo design provided it does deviate too much.

We would like the tag Line "The KALV Electric Way" worked into that signature as a option.
Updates

Reviewing designs and am underwhelmed with the creativiity and designs, this is anyones prize!

Target Market(s)

Corporate / Middle Managers

Industry/Entity Type

Electrical Contracting & Engineering

Colors
FFF300
FFF600
FEFA6F
FFFEC7
FFFEE8

Requirements
Must have
• Must have, First & Last Name of Employee, Title of Employee, Office & Cell Phone Number, Email Address
Nice to have
• Gif Animation

```html
<!DOCTYPE html>
<html lang="en">
<head>
<meta charset="utf-8">
<title>KALV Electric – Email Signature</title>
<link rel="stylesheet" href="https://fonts.googleapis.com/css2?family=Open+Sans:wght@600;700;800&display=swap">
<style>
  :root {
    --paper: #fdfdfd;
    --band: #000000;
    --ink: #333333;
    --label: #e3b52f;
    --photo-top: #e6e8ec;
    --photo-bottom: #c9ccd4;
  }
  * { box-sizing: border-box; margin: 0; padding: 0; }
  html, body {
    width: 1200px;
    height: 559px;
    overflow: hidden;
    background: var(--paper);
  }
  .signature {
    position: relative;
    width: 1200px;
    height: 559px;
    font-family: "Open Sans", Arial, sans-serif;
    color: var(--ink);
    background: var(--paper);
  }
  .signature__band {
    position: absolute;
    left: 0;
    top: 441px;
    width: 1200px;
    height: 118px;
    background: var(--band);
  }
  .portrait {
    position: absolute;
    left: 543px;
    top: 39px;
    width: 160px;
    height: 160px;
    border-radius: 50%;
    background: linear-gradient(180deg, var(--photo-top) 0%, var(--photo-bottom) 100%);
  }
  .identity {
    position: absolute;
    left: 737px;
    top: 72px;
  }
  .identity__name {
    font-size: 50px;
    font-weight: 800;
    line-height: 1;
    letter-spacing: 0.2px;
  }
  .identity__title {
    margin-top: 16px;
    font-size: 27px;
    font-weight: 600;
    line-height: 1;
  }
  .contact {
    position: absolute;
    left: 555px;
    top: 228px;
    list-style: none;
  }
  .contact__item {
    font-size: 25px;
    font-weight: 600;
    line-height: 43px;
    white-space: nowrap;
  }
  .contact__label { color: var(--label); }
  .social {
    position: absolute;
    left: 555px;
    top: 380px;
    display: flex;
    gap: 18px;
    list-style: none;
  }
  .social__item {
    display: flex;
    align-items: center;
    gap: 6px;
    height: 26px;
    font-size: 15px;
    font-weight: 700;
    color: var(--ink);
  }
  .social__mark {
    width: 14px;
    height: 14px;
    border-radius: 3px;
    background: var(--label);
  }
</style>
</head>
<body>
  <main class="signature">
    <div class="portrait" role="img" aria-label="Portrait photo of Daniel Reyes, Project Manager"></div>

    <header class="identity">
      <h1 class="identity__name">Daniel Reyes</h1>
      <p class="identity__title">Project Manager</p>
    </header>

    <ul class="contact">
      <li class="contact__item"><span class="contact__label">Phone:</span> 555-201-4870</li>
      <li class="contact__item"><span class="contact__label">Email:</span> daniel.reyes@kalvelectric.com</li>
      <li class="contact__item"><span class="contact__label">Website:</span> www.kalvelectric.com</li>
    </ul>

    <ul class="social">
      <li class="social__item"><span class="social__mark"></span>Photon</li>
      <li class="social__item"><span class="social__mark"></span>Friendly</li>
      <li class="social__item"><span class="social__mark"></span>Chirper</li>
      <li class="social__item"><span class="social__mark"></span>WorkNet</li>
    </ul>

    <div class="signature__band"></div>
  </main>
</body>
</html>
```